Web Design Project

We need the homepage and 7 interior pages designed as described below - design only:

Main Page
We like this template: http://www.quillbarrow.com/demo/52917.html

We also want a login dropdown similar to http://www.perloxa.com

We want the main page to be luxurious and sleek. We are a limo company that is dedicated to good service and creating an experience, and our front page should strongly reflect that. We do not want a very busy front page.

The main page should do primary things:

1. Make Reservations: We really like velmorta.com for this aspect of the site. That being said, velmorta is NOT the type of company we are.
2. Inform the customer of our most popular packages and give a sense of our professionalism and luxurious service.
3. There should be an area for a customer login
4. Menu should include the following: Home, Who We Are, Our Fleet, Custom Packages,
Testimonials, Book Your Ride!

For a starting point, we like this template http://www.quillbarrow.com/demo/52917.html

Rather than "start up, integrate, develop" we could have 3 of the more popular packages (or categories of packages). The bottom part would be fine. We could have a chirpnet feed, welcome, and our core principles. The one big change would be the addition of a "booking" area right smack in the middle of the page, where a customer could enter in trip data and see if the date was available.

-

About Us - Secondary Page
We like this ABOUT page template: http://www.quillbarrow.com/demo/63284.html

This is a really important page that people overlook, yet it is the most viewed page of a website after the homepage. We have come up with a bit of text to go on the about us page:

Who We Are: Brisbury Limo was founded on the core principle that every limo ride starts with personalized service from the instant you book your ride and continues after you step out of the car. You and your party are more than just our customers. We consider knowing your name and providing you with your choice of snacks and periodicals in the car just a few of the integral elements of the limousine experience. We are striving to revolutionize the limousine industry by creating a personal, friendly, timely, and professional experience. Brisbury Limo combines current technology and a modern fleet with good old-fashioned service to deliver you a personalized, luxury experience. We cater to every event, from business travel to proms and wedding, and everything in between.

We do all of this while maintaining competitive pricing to our peers.

Have a taste of high society...

-

Custom Packages - Secondary Page

This page will contain descriptions of the packages that we offer: Wedding, Prom, Business, etc. - there should be a thumbnail of each package with a description next to it. When you click on a thumbnail it will bring you to a detailed page of that particular package.

-

Custom Packages Interior Page - Secondary Page

In depth look at that particular package - for example, weddings - shows that we offer complimentary champagne, Just married sign, etc.

-

Fleet Page - Secondary Page

This page can be fairly basic. It will include photos of the vehicles along with descriptions and number of passengers, etc.

-

Testimonials Page - Secondary Page

This page will have testimonials from customers. We don't want a big block of text, but rather small testimonials that will expand within the page when you click on a "+" symbol. We like the way it looks when the testimonials are enclosed within a speech bubble image - still professional and classy, not cheesy.

-

Book your ride! - Secondary Page

This page will have a form on it - the same as the form on the homepage, where people can enter in information to check the availability of vehicles. We also want basic contact information on this page as well in case people want to call directly or e-mail.

Requirements
Must have
• - Book your reservation form on homepage
- Sleek, elegant feel
- Chirpnet feed

```html
<!DOCTYPE html>
<html lang="en">
<head>
<meta charset="utf-8">
<title>Brisbury Limo</title>
<link href="https://fonts.googleapis.com/css2?family=Arimo:wght@400;700&family=Roboto+Condensed:wght@400;700&display=swap" rel="stylesheet">
<style>
  :root {
    --bg-deep: #0f1f5c;
    --bg-mid: #16307a;
    --bg-top: #0b5aa8;
    --card: #1a6cc0;
    --card-line: #3d8bd6;
    --panel: #0d2a86;
    --title-light: #a9d4f5;
    --body-light: #9cccf2;
    --text-white: #ffffff;
    --nav-text: #142a66;
    --btn-dark: #12437d;
    --btn-text: #b9dcf7;
    --field: #eef0f3;
    --rule: #0a1a4c;
  }
  * { box-sizing: border-box; margin: 0; padding: 0; }
  html, body { width: 1029px; height: 1200px; overflow: hidden; background: var(--bg-deep); }
  .page {
    position: relative; width: 1200px; height: 1400px;
    transform: scale(0.8575); transform-origin: 0 0;
    background:
      radial-gradient(ellipse 900px 260px at 600px 0, var(--bg-top), transparent 70%),
      linear-gradient(180deg, #123c8f 0, var(--bg-mid) 320px, var(--bg-deep) 1400px);
    font-family: "Arimo", Arial, sans-serif; color: var(--text-white);
  }
  .abs { position: absolute; }

  /* header */
  .login-box { left: 690px; top: -1px; width: 390px; height: 44px; border: 1px solid #3f78c4; border-top: none; border-radius: 0 0 8px 8px; background: rgba(8,40,110,.4); }
  .login-field { position: absolute; top: 9px; height: 23px; width: 144px; background: var(--field); border: 1px solid #c7ccd4; font-size: 12px; color: #555; padding: 5px 6px; }
  .login-btn { position: absolute; left: 309px; top: 8px; width: 70px; height: 26px; background: linear-gradient(#2aa0ef, #0b6bc8); border: 1px solid #5ab7f5; border-radius: 2px; font-family: "Roboto Condensed", sans-serif; font-weight: 700; font-size: 14px; text-align: center; line-height: 24px; }
  .brand-name { left: 130px; top: 58px; font-family: "Arimo", Arial, sans-serif; font-weight: 700; font-size: 26px; color: var(--text-white); }

  /* nav */
  .nav { left: 120px; top: 146px; width: 960px; height: 40px; background: linear-gradient(#fdfdfd, #d8dadd); }
  .nav a { font-family: "Roboto Condensed", sans-serif; font-weight: 700; font-size: 14px; color: var(--nav-text); text-decoration: none; position: absolute; top: 13px; }

  /* booking */
  .booking { left: 120px; top: 185px; width: 300px; height: 341px; background: linear-gradient(160deg, #1546b0, var(--panel) 60%, #081f6b); border: 1px solid #2f7be0; }
  .booking h2 { position: absolute; left: 27px; top: 12px; font-family: "Roboto Condensed", sans-serif; font-weight: 700; font-size: 30px; color: #e8eef8; letter-spacing: -.5px; }
  .tab { position: absolute; top: 66px; height: 26px; font-size: 12.5px; text-align: center; line-height: 26px; }
  .tab-active { left: 29px; width: 107px; background: #0a1f58; color: #fff; }
  .tab-active::after { content: ""; position: absolute; left: 48px; bottom: -6px; border: 6px solid transparent; border-top-color: #0a1f58; border-bottom: 0; }
  .tab-idle { left: 142px; width: 108px; background: linear-gradient(#f5f6f8, #cfd3da); color: #1c2f63; }
  .b-label { position: absolute; font-size: 12.5px; color: #e6ecf7; }
  .b-field { position: absolute; height: 25px; background: linear-gradient(#e3e6ea, #fbfbfc); border: 1px solid #b8c0cc; border-radius: 2px; }
  .calc-btn { position: absolute; left: 69px; top: 290px; width: 181px; height: 33px; background: linear-gradient(#ffffff, #cfd3d8); border-radius: 3px; color: #142a66; font-family: "Roboto Condensed", sans-serif; font-weight: 700; font-size: 15px; text-align: center; line-height: 33px; }
  .hero-photo { left: 420px; top: 185px; width: 660px; height: 341px; background: linear-gradient(180deg, #4f5a3b 0, #7c8a6a 25%, #d9dde0 50%, #aeb3b7 75%, #3c3f3d 100%); }

  /* packages */
  .pkg { top: 546px; width: 300px; height: 362px; background: var(--card); }
  .pkg h3 { height: 53px; border-bottom: 1px solid var(--card-line); text-align: center; font-size: 24px; font-weight: 700; color: var(--title-light); line-height: 56px; }
  .pkg-photo { position: absolute; left: 28px; top: 74px; width: 240px; height: 120px; border: 4px solid #2a86d8; }
  .pkg p { position: absolute; left: 10px; right: 6px; top: 219px; text-align: center; font-size: 14px; line-height: 17px; color: var(--body-light); }
  .pkg-more { position: absolute; left: 108px; top: 309px; width: 79px; height: 30px; }
  .btn-more { background: var(--btn-dark); border: 1px solid #3f8fdc; color: var(--btn-text); font-weight: 700; font-size: 14px; text-align: center; line-height: 28px; }

  /* lower */
  .sec-title { top: 943px; font-size: 24px; font-weight: 700; color: var(--title-light); }
  .sec-photo { top: 997px; width: 300px; height: 140px; border: 5px solid #1b84dc; }
  .sec-text { font-size: 12px; line-height: 18px; color: #e9eef8; width: 300px; }
  .arrow { top: 946px; width: 23px; height: 22px; }
  .divider-dots { left: 780px; width: 300px; border-top: 1px dashed #3f78c4; }
  .sig { left: 781px; top: 1206px; font-size: 14px; font-weight: 700; }

  /* footer */
  .footer-rule { left: 120px; top: 1334px; width: 960px; height: 2px; background: var(--rule); }
  .footer-text { top: 1363px; font-size: 12.5px; color: #8fc2ee; }
</style>
</head>
<body>
<div class="page">

  <header>
    <div class="abs login-box">
      <div class="login-field" style="left:10px">username</div>
      <div class="login-field" style="left:159px">Password</div>
      <div class="login-btn">LOGIN</div>
    </div>
    <div class="abs brand-name">Brisbury Limo</div>
  </header>

  <nav class="abs nav">
    <a style="left:58px">HOME</a>
    <a style="left:162px">WHO WE ARE</a>
    <a style="left:308px">OUR FLEET</a>
    <a style="left:441px">CUSTOM PACKAGES</a>
    <a style="left:630px">TESTIMONIALS</a>
    <a style="left:789px">BOOK YOUR RIDE!</a>
  </nav>

  <section class="abs booking">
    <h2>BOOK YOUR RIDE!</h2>
    <div class="tab tab-active">ONE WAY</div>
    <div class="tab tab-idle">BY THE HOUR</div>
    <div class="b-label" style="left:31px;top:108px">PICK UP</div>
    <div class="b-field" style="left:30px;top:131px;width:238px"></div>
    <div class="b-label" style="left:31px;top:166px">DROP OFF</div>
    <div class="b-field" style="left:30px;top:189px;width:238px"></div>
    <div class="b-label" style="left:28px;top:225px">PICKUP DATE</div>
    <div class="b-label" style="left:162px;top:225px">PICKUP TIME</div>
    <div class="b-field" style="left:29px;top:247px;width:106px"></div>
    <div class="b-field" style="left:162px;top:247px;width:106px"></div>
    <div class="calc-btn">CALCULATE PRICES</div>
  </section>
  <div class="abs hero-photo" role="img" aria-label="White stretch limousine parked by a garden"></div>

  <section class="abs pkg" style="left:120px">
    <h3>WEDDING</h3>
    <div class="pkg-photo" role="img" aria-label="Bride and groom seated inside a limousine" style="background:linear-gradient(135deg,#3a4f7a,#c9c6c2 55%,#f2efea)"></div>
    <p>Lorem ipsm dolor s amet, consectetur asicing elit, iliised itlui do eiusmod tempor incididunt ut laboiet dolore magna aliqua. Ut enim ad minim veniamiLor......</p>
    <div class="pkg-more btn-more">MORE</div>
  </section>
  <section class="abs pkg" style="left:450px">
    <h3>BACHELOR</h3>
    <div class="pkg-photo" role="img" aria-label="Group of friends celebrating inside a limousine" style="background:linear-gradient(135deg,#7a2a22,#c6453a 45%,#d8c7b6)"></div>
    <p>Lorem ipsm dolor s amet, consectetur asicing elit, iliised itlui do eiusmod tempor incididunt ut laboiet dolore magna aliqua. Ut enim ad minim veniamiLor......</p>
    <div class="pkg-more btn-more">MORE</div>
  </section>
  <section class="abs pkg" style="left:780px">
    <h3>CORPORATE</h3>
    <div class="pkg-photo" role="img" aria-label="Business travellers working on a laptop in a limousine" style="background:linear-gradient(135deg,#5c5648,#d8d0bf 55%,#3a3a3a)"></div>
    <p>Lorem ipsm dolor s amet, consectetur asicing elit, iliised itlui do eiusmod tempor incididunt ut laboiet dolore magna aliqua. Ut enim ad minim veniamiLor......</p>
    <div class="pkg-more btn-more">MORE</div>
  </section>

  <section>
    <h3 class="abs sec-title" style="left:121px">WELCOME!</h3>
    <div class="abs sec-photo" style="left:119px;background:linear-gradient(90deg,#f4e7c9,#e9d9c6 50%,#c9a58c)" role="img" aria-label="Smiling chauffeur with team in the background"></div>
    <p class="abs sec-text" style="left:120px;top:1153px">Sed ut perspiciatis unde omnis iste natus error sit volup-tatem accusantium doloremque laudantium, totam remil aperiam, eaque ipsa quae ab illo inventore veritatis etiltí quasi architecto beatae vitae dicta sunt expl Nemo enim s sit as pernatur aut oditi aut fugit.....</p>
    <div class="abs btn-more" style="left:121px;top:1284px;width:80px;height:30px">MORE</div>
  </section>

  <section>
    <h3 class="abs sec-title" style="left:450px">OUR FLEET</h3>
    <div class="abs sec-photo" style="left:450px;background:linear-gradient(180deg,#6f7a5c,#4a1e2a 45%,#2a1a1e 75%,#6b6b63)" role="img" aria-label="Dark red stretch SUV limousine"></div>
    <p class="abs sec-text" style="left:450px;top:1153px">Sed ut perspiciatis unde omnis iste natus error sit volup-tatem accusantium doloremque laudantium, totam remil aperiam, eaque ipsa quae ab illo inventore veritatis etiltí quasi architecto beatae vitae dicta sunt expl Nemo enim ia voluptas sit as pernatur aut oditi aut fugit,...</p>
    <div class="abs btn-more" style="left:451px;top:1284px;width:80px;height:30px">MORE</div>
  </section>

  <section>
    <h3 class="abs sec-title" style="left:780px">TESTIMONIALS</h3>
    <svg class="abs arrow" style="left:1030px" viewBox="0 0 23 22"><rect width="23" height="22" fill="#13368a"/><path d="M13 8l-3 3 3 3" stroke="#9cc3ee" stroke-width="1.5" fill="none"/></svg>
    <svg class="abs arrow" style="left:1056px" viewBox="0 0 23 22"><rect width="23" height="22" fill="#1577d4"/><path d="M10 8l3 3-3 3" stroke="#fff" stroke-width="1.5" fill="none"/></svg>
    <p class="abs sec-text" style="left:780px;top:992px">Sed ut perspiciatis unde omnis iste natus error sit volup-tatem accusantium doloremque laudantium, totam remil aperiam, eaque ipsa quae ab illo inventore veritatis etiltí quasi architecto beatae vitae dicta sunt expl Nemo enim ipsam voluptatem quia voluptas sit as pernatur aut oditi aut fugit,...</p>
    <p class="abs sec-text" style="left:780px;top:1118px">Sed ut perspiciatis unde omnis iste natus error sit volup-tatem accusantium doloremque laudantium, totam remil aperiam, eaque ipsa quae ab illo inventore veritatis etiltí quasi ,...</p>
    <div class="abs divider-dots" style="top:1198px"></div>
    <div class="abs sig">M.W.</div>
    <div class="abs divider-dots" style="top:1230px"></div>
    <div class="abs btn-more" style="left:780px;top:1284px;width:80px;height:30px">MORE</div>
  </section>

  <footer>
    <div class="abs footer-rule"></div>
    <div class="abs footer-text" style="left:120px">© 2012 Brisburylimo. All Rights Reserved.</div>
    <div class="abs footer-text" style="left:966px">Privacy Policy &nbsp;| T&amp;C</div>
  </footer>

</div>
</body>
</html>
```